FR banner

we need a banner design (36"x120" horizontal) that will be displayed on a local high school baseball field. My company ( Crestwell Prints Co) has been producing signage for the Fernmoor Ridge community since 2009. We would like to communicate that we do more than banners. The final design should include the slogan "Signs Shirts Swag" and our Logo.

Target Market(s)

companies, teams, events, shirt and other marketing items.

Industry/Entity Type

Sign, Print,

Font styles to use
Sans Serif

Requirements
Should not have
• no baseball content.

```html
<!DOCTYPE html>
<html lang="en">
<head>
<meta charset="utf-8">
<title>Crestwell Prints Co — Field Banner</title>
<link rel="stylesheet" href="https://fonts.googleapis.com/css2?family=Archivo:ital,wdth,wght@0,125,900;1,125,900&display=swap">
<style>
  :root {
    --page: #eef1f5;
    --navy: #1c2a8c;
    --violet: #4a1f6e;
    --crimson: #8c0f12;
    --red: #a30c0c;
    --ink: #0d1347;
    --white: #ffffff;
    --silver: #c9ccd3;
    --shadow: rgba(20, 0, 10, 0.45);
  }
  * { margin: 0; padding: 0; box-sizing: border-box; }
  html, body {
    width: 1200px;
    height: 800px;
    overflow: hidden;
    background: var(--page);
  }
  .banner {
    position: absolute;
    left: 40px;
    top: 232px;
    width: 1120px;
    height: 336px;
    overflow: hidden;
    background: linear-gradient(100deg, var(--navy) 0%, var(--violet) 38%, var(--crimson) 75%, var(--red) 100%);
    box-shadow: 0 6px 20px rgba(0, 0, 0, 0.18);
  }
  .long-shadow {
    position: absolute;
    inset: 0;
    width: 100%;
    height: 100%;
  }
  .brand {
    position: absolute;
    left: 70px;
    top: 0;
    height: 100%;
    width: 330px;
    display: flex;
    align-items: center;
    gap: 22px;
  }
  .brand-mark {
    flex: none;
    width: 64px;
    height: 64px;
    background: var(--white);
  }
  .brand-name {
    font-family: "Archivo", sans-serif;
    font-weight: 900;
    font-stretch: 125%;
    font-style: normal;
    font-size: 38px;
    line-height: 1.05;
    color: var(--white);
    text-transform: uppercase;
  }
  .slogan {
    position: absolute;
    left: 470px;
    top: 24px;
    font-family: "Archivo", sans-serif;
    font-weight: 900;
    font-stretch: 125%;
    font-style: italic;
    font-size: 96px;
    line-height: 0.99;
    text-transform: uppercase;
    letter-spacing: 1px;
  }
  .slogan-line {
    display: block;
    background: linear-gradient(180deg, var(--white) 0%, var(--white) 45%, var(--silver) 50%, var(--white) 80%);
    -webkit-background-clip: text;
    background-clip: text;
    color: transparent;
    -webkit-text-stroke: 3px var(--ink);
    paint-order: stroke fill;
  }
</style>
</head>
<body>
  <section class="banner" aria-label="Crestwell Prints Co field banner">
    <svg class="long-shadow" viewBox="0 0 1120 336" preserveAspectRatio="none" aria-hidden="true">
      <polygon points="470,40 900,40 1120,190 1120,336 640,336 470,250" fill="var(--shadow)"/>
    </svg>

    <div class="brand">
      <span class="brand-mark" aria-hidden="true"></span>
      <p class="brand-name">Crestwell<br>Prints Co</p>
    </div>

    <h1 class="slogan">
      <span class="slogan-line">Signs</span>
      <span class="slogan-line">Shirts</span>
      <span class="slogan-line">Swag</span>
    </h1>
  </section>
</body>
</html>
```